German Headhunter/ HR Consultancy needs Business Cards Design

We need a business Card Design for our Company in Stuttgart. We are specialized as Headhunter/ HR Consultancy in Placement of specialist and managers in permanent employment. Please refer to our business logo.

```html
<!DOCTYPE html>
<html lang="en">
<head>
<meta charset="utf-8">
<title>Kernwerk Personalberatung – Business Card</title>
<link href="https://fonts.googleapis.com/css2?family=Montserrat:wght@500;600&family=Arimo:wght@400&display=swap" rel="stylesheet">
<style>
  :root{
    --stage:#b8b8b8;
    --paper:#ffffff;
    --brand-blue:#3a55a5;
    --ink-grey:#4a4a4a;
    --rule-grey:#9a9a9a;
    --white:#ffffff;
  }
  *{margin:0;padding:0;box-sizing:border-box}
  html,body{width:1075px;height:1200px;overflow:hidden;background:var(--stage)}
  .card{position:absolute;left:206px;width:663px;height:395px;overflow:hidden}
  .card--front{top:187px;background:var(--paper)}
  .card--back{top:637px;background:var(--brand-blue)}

  .brand{position:absolute;display:flex;align-items:center;gap:16px;
    font-family:"Montserrat",sans-serif;font-weight:600;line-height:1}
  .brand__mark{width:52px;height:52px;flex:none}
  .brand__name{font-size:38px;letter-spacing:1px}
  .brand__sub{font-size:17px;letter-spacing:.5px;margin-top:6px}
  .card--front .brand{left:300px;top:88px;color:var(--brand-blue)}
  .card--front .brand__mark{background:var(--brand-blue)}
  .card--back .brand{left:150px;top:164px;color:var(--white)}
  .card--back .brand__mark{background:var(--white);width:62px;height:62px}
  .card--back .brand__name{font-size:46px}
  .card--back .brand__sub{font-size:21px}

  .holder{position:absolute;left:35px;top:196px}
  .holder__name{font-family:"Montserrat",sans-serif;font-weight:600;font-size:25px;color:var(--brand-blue);letter-spacing:.3px}
  .holder__role{font-family:"Arimo",sans-serif;font-size:16px;color:var(--ink-grey);margin-top:2px;letter-spacing:.3px}
  .holder__rule{position:absolute;left:35px;top:258px;width:225px;height:4px;background:var(--rule-grey)}

  .band{position:absolute;left:0;top:260px;width:100%;height:135px;background:var(--brand-blue);
    font-family:"Arimo",sans-serif;font-size:18px;color:var(--white)}
  .contact{position:absolute;left:35px;top:28px;list-style:none}
  .contact li{display:flex;align-items:center;gap:6px;height:23.5px}
  .contact svg{width:17px;height:17px;flex:none}
  .address{position:absolute;right:42px;top:55px;text-align:right;line-height:23px;font-style:normal}
</style>
</head>
<body>
  <section class="card card--front">
    <div class="brand">
      <span class="brand__mark"></span>
      <div><div class="brand__name">KERNWERK</div><div class="brand__sub">PERSONALBERATUNG</div></div>
    </div>
    <div class="holder">
      <div class="holder__name">JONAS WEBER</div>
      <div class="holder__role">MANAGING DIRECTOR</div>
    </div>
    <div class="holder__rule"></div>
    <div class="band">
      <ul class="contact">
        <li><svg viewBox="0 0 24 24" fill="none" stroke="currentColor" stroke-width="2"><path d="M5 3h4l2 5-2.5 1.5a11 11 0 0 0 6 6L16 13l5 2v4a2 2 0 0 1-2 2A17 17 0 0 1 3 5a2 2 0 0 1 2-2z"/></svg>044-123 456 789</li>
        <li><svg viewBox="0 0 24 24" fill="currentColor"><path d="M2 5h20v14H2z M3 6l9 7 9-7" stroke="var(--brand-blue)" stroke-width="1.5"/></svg>info@webname.com</li>
        <li><svg viewBox="0 0 24 24" fill="none" stroke="currentColor" stroke-width="1.8"><circle cx="12" cy="12" r="9.5"/><ellipse cx="12" cy="12" rx="4" ry="9.5"/><path d="M2.5 12h19M4 7h16M4 17h16"/></svg>www.websitename.com</li>
      </ul>
      <address class="address">421, Address line goes here<br>45452,Country Name</address>
    </div>
  </section>

  <section class="card card--back">
    <div class="brand">
      <span class="brand__mark"></span>
      <div><div class="brand__name">KERNWERK</div><div class="brand__sub">PERSONALBERATUNG</div></div>
    </div>
  </section>
</body>
</html>
```